trading data display webpage

We have build a rough wireframe of the two webpages that we want to display .The two wireframes are attached as a pdf document.
there will be login page. after login , the user will see the index page. that is the first page of the wireframe.

what we are displaying is essentially spread data. we are taking the difference in prices are two places and displaying the data. some calculations are done and is shown in the grid.

below the grid we show the behaviour on a graph. we will use bubble chart. I did not find a sample, hence have thrown in a placeholder.

this is time series data ( changes daily) and hence we need to check the behaviour.

the second wire frame shows how the user will choose the source price points and the destination price points.
we are talking here of natural gas prices hence the reference to source prices and destination prices.

you need to design the page/ pages such that the end-user loves it and is easy to use. the intent here is easy to use and easy to understand.
this will be responsive webpage since the end user will check it out on a tablet or a smartphone.

so if possible tell us how the navigation bar, the button bar, etc should fall when the screen size decreases.

I have uploaded 2 files. one is the wireframe ( pdf document) and second is the logo file.

please also let us know where to place the logo.

Target Market(s)

the target market is traders and data analyst

Industry/Entity Type

Build

Colors

Designer to choose colors to be used in the design.

Requirements
Must have
• 1. design for the web.
2. but think how the design will look when the screen size decreases.
3. tell if possible what screen components to keep and what to hide.

```html
<!DOCTYPE html>
<html lang="en">
<head>
<meta charset="utf-8">
<title>Spreadline – Sign in</title>
<link rel="stylesheet" href="https://fonts.googleapis.com/css2?family=Open+Sans:wght@400;600;700&display=swap">
<style>
  :root {
    --bg-light: #ffffff;
    --bg-mid: #f0f0f0;
    --bg-dark: #e4e4e4;
    --accent-orange: #f26522;
    --accent-green: #8cc63f;
    --accent-green-dark: #76b32c;
    --brand-text: #555a60;
    --link-red: #f0525a;
    --panel-bg: #f2f2f2;
    --panel-border: #dcdcdc;
    --field-bg: #ffffff;
    --placeholder: #b3b3b3;
    --dot: #c2c2c2;
    --white: #ffffff;
  }
  * { box-sizing: border-box; margin: 0; padding: 0; }
  html, body { width: 1200px; height: 720px; overflow: hidden; }
  body {
    font-family: "Open Sans", Arial, sans-serif;
    background: radial-gradient(ellipse 520px 420px at 600px 110px, var(--bg-light) 0%, var(--bg-mid) 55%, var(--bg-dark) 100%);
    background-color: var(--bg-dark);
    position: relative;
  }
  .brand {
    position: absolute;
    left: 0; right: 0; top: 124px;
    text-align: center;
  }
  .brand-name {
    font-size: 40px; font-weight: 600; color: var(--brand-text);
    line-height: 1;
  }
  .login-panel {
    position: absolute;
    left: 434px; top: 305px; width: 333px; height: 172px;
    background: var(--panel-bg);
    border: 1px solid var(--panel-border);
    border-radius: 3px;
    box-shadow: 0 4px 8px rgba(0,0,0,0.06);
  }
  .field {
    position: absolute; left: 9px; width: 313px; height: 41px;
    display: flex; background: var(--field-bg); border-radius: 2px;
    box-shadow: 0 3px 5px rgba(0,0,0,0.07);
  }
  .field--email { top: 9px; }
  .field--password { top: 60px; }
  .field-icon {
    width: 51px; height: 100%; background: var(--accent-orange);
    display: flex; align-items: center; justify-content: center;
    border-radius: 2px 0 0 2px;
  }
  .field-input {
    flex: 1; display: flex; align-items: center; padding-left: 16px;
    font-size: 13.5px; color: var(--placeholder);
  }
  .password-dots { display: flex; gap: 4.3px; }
  .password-dots span { width: 7px; height: 7px; border-radius: 50%; background: var(--dot); }
  .field-status { width: 34px; display: flex; align-items: center; justify-content: center; }
  .sign-in {
    position: absolute; left: 10px; top: 116px; width: 173px; height: 40px;
    background: linear-gradient(var(--accent-green), var(--accent-green-dark));
    border: 1px solid #7db53a; border-radius: 2px;
    color: var(--white); font-family: inherit; font-size: 15px; font-weight: 600;
    text-shadow: 0 1px 1px rgba(0,0,0,0.15);
  }
  .aux-links {
    position: absolute; left: 243px; top: 126px;
    display: flex; flex-direction: column; align-items: flex-start; gap: 4px;
  }
  .aux-links a {
    font-size: 9.5px; line-height: 13px; color: var(--link-red); text-decoration: underline;
  }
  .aux-links a:last-child { margin-left: 1px; }
</style>
</head>
<body>
  <header class="brand">
    <span class="brand-name">Spreadline</span>
  </header>

  <form class="login-panel">
    <div class="field field--email">
      <span class="field-icon">
        <svg width="20" height="18" viewBox="0 0 20 18"><circle cx="10" cy="5" r="4.5" fill="#fff"/><path d="M1 18c0-5 4-8 9-8s9 3 9 8z" fill="#fff"/></svg>
      </span>
      <span class="field-input">e-mail</span>
      <span class="field-status">
        <svg width="17" height="17" viewBox="0 0 17 17"><circle cx="8.5" cy="8.5" r="8.5" fill="#8cc63f"/><path d="M4.5 8.8l2.6 2.6 5-5" stroke="#fff" stroke-width="2" fill="none"/></svg>
      </span>
    </div>
    <div class="field field--password">
      <span class="field-icon">
        <svg width="14" height="19" viewBox="0 0 14 19"><path d="M3.5 8V5a3.5 3.5 0 0 1 7 0v3" stroke="#fff" stroke-width="2" fill="none"/><rect x="0" y="8" width="14" height="11" rx="1" fill="#fff"/></svg>
      </span>
      <span class="field-input">
        <span class="password-dots"><span></span><span></span><span></span><span></span><span></span><span></span><span></span><span></span><span></span><span></span><span></span></span>
      </span>
      <span class="field-status">
        <svg width="17" height="17" viewBox="0 0 17 17"><circle cx="8.5" cy="8.5" r="8.5" fill="#f0525a"/><path d="M5.8 5.8l5.4 5.4M11.2 5.8l-5.4 5.4" stroke="#fff" stroke-width="2"/></svg>
      </span>
    </div>
    <button type="button" class="sign-in">Sign in</button>
    <nav class="aux-links">
      <a href="#">Register now</a>
      <a href="#">Forget Password?</a>
    </nav>
  </form>
</body>
</html>
```